Driving School Business card design

Hi, we are starting a new business (Driving School) and would like your help with our business card design.
We are located in Adelaide SA.
Our aim is to help young people achieve best possible results by promoting safe and stress free driving.

Name of our school is "Velmira" which means best or most favorable.

Hope there is someone out there in wonderful world of design who can think outside of square and give us recognizable/ unique business card design.

Target Market(s)

16+

Industry/Entity Type

Business

Contact Information for Business Card

Name of our business is "Velmira driver training"
Our idea is to make letter "L' in Velmira more distinct (noticeable) by different color or font, so it gets associated with learner driver.
We like combination of white, dark gray and yellow but do not limit our self to that.
Reverse side of our card would have to incorporate writing space for date and time of the next lesson.

Requirements
Must have
• Business name: Velmira driver training
• Owner/ instructor name
• Mobile no:
• Chatterloop logo
Should not have
• Anything Not associated with driving

```html
<!DOCTYPE html>
<html lang="en">
<head>
<meta charset="utf-8">
<title>Velmira driver training – Business card</title>
<link rel="stylesheet" href="https://fonts.googleapis.com/css2?family=Open+Sans:wght@300;400;600;700&display=swap">
<style>
  :root {
    --page-bg: #2a2a2c;
    --card-white: #f3f5f4;
    --asphalt-dark: #1b1e22;
    --asphalt-mid: #2e3238;
    --asphalt-light: #3a3f45;
    --overlay-gray: rgba(120, 124, 130, 0.45);
    --brand-yellow: #f7e51d;
    --edge-amber: #e0a41a;
    --ribbon-shade: #c9b514;
    --ink-dark: #2b2b2b;
    --icon-gray: #6b6f73;
    --text-light: #f2f2f2;
  }
  * { box-sizing: border-box; margin: 0; padding: 0; }
  html, body {
    width: 1200px; height: 1000px; overflow: hidden;
    background: var(--page-bg);
    font-family: "Open Sans", Arial, sans-serif;
  }
  .canvas {
    position: relative; width: 1200px; height: 1000px;
  }
  .card {
    position: absolute; left: 215px; width: 770px; height: 440px;
    border-radius: 18px; overflow: hidden;
    box-shadow: 0 12px 30px rgba(0,0,0,0.45);
  }
  .card--front { top: 40px; background: var(--card-white); }
  .card--back { top: 520px; }

  /* Front */
  .road-panel {
    position: absolute; top: 0; right: 0; width: 420px; height: 100%;
    background: radial-gradient(ellipse at 60% 40%, var(--asphalt-mid), var(--asphalt-dark) 75%);
    clip-path: polygon(20px 0, 100% 0, 100% 100%, 0 100%);
  }
  .road-edge {
    position: absolute; top: 0; left: 344px; width: 12px; height: 100%;
    background: var(--edge-amber);
    clip-path: polygon(6px 0, 12px 0, 6px 100%, 0 100%);
  }
  .road-panel__band {
    position: absolute; left: 0; right: 0; top: 300px; height: 90px;
    background: var(--overlay-gray);
  }
  .info-ribbon {
    position: absolute; left: 0; top: 228px; width: 400px; height: 74px;
    background: var(--brand-yellow);
  }
  .info-ribbon__fold {
    position: absolute; left: 350px; top: 302px; width: 50px; height: 16px;
    background: var(--ribbon-shade);
    clip-path: polygon(0 0, 100% 0, 0 100%);
  }
  .identity {
    position: absolute; left: 70px; top: 66px;
    padding-left: 16px; border-left: 5px solid var(--brand-yellow);
    color: var(--ink-dark);
  }
  .identity__name { font-size: 30px; font-weight: 400; line-height: 1; letter-spacing: 0.5px; }
  .identity__role { font-size: 17px; font-weight: 400; letter-spacing: 1px; margin-top: 4px; }

  .contact-row {
    position: absolute; left: 70px; display: flex; align-items: center; gap: 18px;
    color: var(--ink-dark);
  }
  .contact-row--phone { top: 150px; }
  .contact-row--web { top: 238px; }
  .contact-row--address { top: 330px; }
  .contact-icon {
    width: 44px; height: 44px; border-radius: 8px; background: var(--icon-gray);
    display: flex; align-items: center; justify-content: center; flex: none;
  }
  .contact-text { font-size: 17px; line-height: 1.25; font-weight: 600; }
  .contact-text--address { font-size: 20px; font-weight: 400; }

  /* Back */
  .back-road {
    position: absolute; inset: 0;
    background: radial-gradient(ellipse at 50% 35%, var(--asphalt-light), var(--asphalt-dark) 80%);
  }
  .back-band {
    position: absolute; left: 0; right: 0; bottom: 0; height: 90px;
    background: var(--overlay-gray);
  }
  .back-side-band {
    position: absolute; right: 0; top: 150px; width: 260px; height: 200px;
    background: var(--overlay-gray); opacity: 0.6;
  }
  .back-title {
    position: absolute; left: 150px; top: 190px; width: 460px; text-align: center;
    color: var(--text-light); font-size: 34px; font-weight: 300; letter-spacing: 1px;
    transform: rotate(-33deg);
  }
  .appointment {
    position: absolute; right: 40px; top: 220px; width: 240px;
    color: var(--ink-dark); font-weight: 700; font-size: 17px;
  }
  .appointment__row { display: flex; align-items: flex-end; gap: 8px; margin-bottom: 22px; }
  .appointment__line { flex: 1; border-bottom: 1.5px solid var(--brand-yellow); height: 18px; }
  .appointment__label { color: var(--text-light); }
</style>
</head>
<body>
<main class="canvas">

  <section class="card card--front" aria-label="Business card front">
    <div class="road-panel" role="img" aria-label="Photograph of asphalt road with yellow centre lines">
      <div class="road-panel__band"></div>
    </div>
    <div class="road-edge"></div>
    <div class="info-ribbon"></div>
    <div class="info-ribbon__fold"></div>

    <div class="identity">
      <p class="identity__name">YOUR NAME</p>
      <p class="identity__role">DESIGNATION</p>
    </div>

    <div class="contact-row contact-row--phone">
      <span class="contact-icon">
        <svg width="26" height="26" viewBox="0 0 24 24" aria-hidden="true">
          <path fill="#fff" d="M6.6 10.8a15.1 15.1 0 0 0 6.6 6.6l2.2-2.2a1 1 0 0 1 1-.25 11.4 11.4 0 0 0 3.6.57 1 1 0 0 1 1 1V20a1 1 0 0 1-1 1A17 17 0 0 1 3 4a1 1 0 0 1 1-1h3.5a1 1 0 0 1 1 1c0 1.25.2 2.45.57 3.57a1 1 0 0 1-.25 1z"/>
        </svg>
      </span>
      <p class="contact-text">+012 345 678 102<br>+012 345 678 102</p>
    </div>

    <div class="contact-row contact-row--web">
      <span class="contact-icon">
        <svg width="28" height="28" viewBox="0 0 24 24" aria-hidden="true">
          <circle cx="12" cy="12" r="9" fill="none" stroke="#fff" stroke-width="1.8"/>
          <ellipse cx="12" cy="12" rx="4" ry="9" fill="none" stroke="#fff" stroke-width="1.4"/>
          <line x1="3" y1="12" x2="21" y2="12" stroke="#fff" stroke-width="1.4"/>
        </svg>
      </span>
      <p class="contact-text">velmiradriver@email.com<br>velmiradriver.com</p>
    </div>

    <div class="contact-row contact-row--address">
      <span class="contact-icon">
        <svg width="26" height="26" viewBox="0 0 24 24" aria-hidden="true">
          <path fill="#fff" d="M12 2a7 7 0 0 0-7 7c0 5.2 7 13 7 13s7-7.8 7-13a7 7 0 0 0-7-7zm0 9.5A2.5 2.5 0 1 1 12 6.5a2.5 2.5 0 0 1 0 5z"/>
        </svg>
      </span>
      <p class="contact-text contact-text--address">ur address goes here<br>street,Crossroad123.</p>
    </div>
  </section>

  <section class="card card--back" aria-label="Business card back">
    <div class="back-road" role="img" aria-label="Photograph of asphalt road with yellow centre lines"></div>
    <div class="back-side-band"></div>
    <div class="back-band"></div>
    <h1 class="back-title">VELMIRA DRIVER TRAINING</h1>
    <div class="appointment">
      <div class="appointment__row"><span class="appointment__label">DATE:</span><span class="appointment__line"></span></div>
      <div class="appointment__row"><span class="appointment__label">TIME:</span><span class="appointment__line"></span></div>
    </div>
  </section>

</main>
</body>
</html>
```